Bright Tykes Flyer - 2 WEEK FREE TRIAL

FLYER - We need a 1 page DL flyer with images and text. Have flyer in landscape

OFFER - 2 WEEK FREE TRIAL

HOW TO GET
Book online now at www.brighttykesplay.com.au/booking

TAG -Where Kids are Champions

PRIZE
Chance to win Full Term of 10 weekly sessions

GIVEAWAYS
Chance to get giveaways such as tickets to games, footballs or other great offers.

LOGO - Attached

Target Market(s)

Parents of children from 5 to 16

Industry/Entity Type

Fitness

Colors
0455a3
ffc214

Requirements
Must have
• Attraction for parents to go online and sign up their kids
Should not have
• Not dull or boring

```html
<!DOCTYPE html>
<html lang="en">
<head>
<meta charset="utf-8">
<title>Bright Tykes Flyer – 2 Week Free Trial</title>
<link rel="stylesheet" href="https://fonts.googleapis.com/css2?family=Black+Ops+One&family=Oswald:wght@500;700&family=Roboto+Condensed:wght@400;700&display=swap">
<style>
  :root {
    --navy: #0455a3;
    --navy-deep: #1a2a6c;
    --gold: #ffc214;
    --gold-pale: #e8d35a;
    --ink: #111111;
    --white: #ffffff;
    --backdrop: #5a5a5a;
  }
  * { margin: 0; padding: 0; box-sizing: border-box; }
  html, body { width: 1200px; height: 708px; overflow: hidden; }
  body { background: var(--backdrop); position: relative; font-family: "Roboto Condensed", sans-serif; }

  .flyer {
    position: absolute; left: 70px; top: 96px;
    width: 1060px; height: 515px;
    background: var(--white); overflow: hidden;
  }
  .flyer-shapes { position: absolute; inset: 0; }

  .trial-badge { position: absolute; left: 85px; top: 15px; width: 230px; height: 230px; }
  .trial-badge__text {
    position: absolute; inset: 0;
    display: flex; flex-direction: column; align-items: center; justify-content: center;
    color: var(--navy-deep); font-family: "Oswald", sans-serif; font-weight: 700;
    line-height: 1; white-space: nowrap;
  }
  .trial-badge__row { display: flex; align-items: flex-end; }
  .trial-badge__num { font-size: 84px; letter-spacing: -2px; }
  .trial-badge__unit { font-size: 38px; margin-left: 4px; margin-bottom: 10px; }
  .trial-badge__label { font-size: 38px; margin-top: 2px; }

  .headline {
    position: absolute; left: 395px; top: 30px; width: 620px;
    text-align: center; white-space: nowrap; font-weight: normal;
  }
  .headline__top {
    display: block;
    font-family: "Black Ops One", sans-serif; color: var(--navy-deep);
    font-size: 72px; line-height: 1; letter-spacing: 2px;
    transform: scaleY(1.55); transform-origin: center top;
  }
  .headline__bottom {
    display: block;
    font-family: "Oswald", sans-serif; font-weight: 700; color: var(--ink);
    font-size: 62px; line-height: 1; margin-top: 54px; letter-spacing: 6px;
    padding-left: 40px;
  }

  .prize-intro {
    position: absolute; left: 122px; top: 252px; white-space: nowrap;
    font-family: "Roboto Condensed", sans-serif; font-weight: 700;
    color: var(--navy-deep); font-size: 31px; line-height: 1.2;
  }
  .prize-box {
    position: absolute; left: 115px; top: 302px; width: 530px; height: 64px;
    background: var(--gold-pale); border-radius: 8px;
    display: flex; align-items: center; justify-content: center;
    white-space: nowrap; overflow: hidden;
  }
  .prize-box__text {
    display: block;
    font-family: "Black Ops One", sans-serif; font-size: 33px; line-height: 1;
    color: var(--ink); letter-spacing: 1px;
    transform: scaleY(1.45);
  }
  .giveaways {
    position: absolute; left: 125px; top: 374px; white-space: nowrap;
    font-size: 15.5px; font-weight: 700; color: var(--ink);
  }

  .brand-row {
    position: absolute; left: 455px; top: 412px; display: flex; gap: 10px;
  }
  .brand-mark {
    display: flex; align-items: center; gap: 4px;
    font-family: "Roboto Condensed", sans-serif; font-weight: 700;
    font-size: 13px; color: var(--navy-deep); white-space: nowrap;
  }
  .brand-mark__dot { width: 10px; height: 10px; border-radius: 50%; background: var(--gold); }

  .booking {
    position: absolute; left: 133px; top: 464px; white-space: nowrap;
    font-family: "Oswald", sans-serif; font-weight: 500; line-height: 1.4;
  }
  .booking__label { color: var(--white); font-size: 14px; text-transform: uppercase; }
  .booking__url { color: var(--gold); font-size: 15px; }

  .photo { position: absolute; }
  .photo--player {
    left: 14px; top: 205px; width: 110px; height: 285px;
    background: linear-gradient(180deg, #8a5a48 0%, #c8242a 26%, #c8242a 55%, #2a2a2a 68%, #d2232a 88%);
    border-radius: 40px 40px 10px 10px;
  }
  .photo--ball {
    left: 134px; top: 410px; width: 48px; height: 46px; border-radius: 50%;
    background: radial-gradient(circle at 40% 40%, #f2f2f2, #9a9a9a);
  }
</style>
</head>
<body>
  <main class="flyer">
    <svg class="flyer-shapes" viewBox="0 0 1060 515" width="1060" height="515" aria-hidden="true">
      <defs>
        <linearGradient id="grunge-gold" x1="0" y1="0" x2="1" y2="1">
          <stop offset="0" stop-color="#e0c948"/>
          <stop offset="0.5" stop-color="#cdb43a"/>
          <stop offset="1" stop-color="#bfa534"/>
        </linearGradient>
        <linearGradient id="field" x1="0" y1="0" x2="0" y2="1">
          <stop offset="0" stop-color="#3f5a2e"/>
          <stop offset="0.55" stop-color="#5e7a3e"/>
          <stop offset="1" stop-color="#86a25a"/>
        </linearGradient>
      </defs>
      <polygon points="0,0 400,0 110,250 0,262" fill="var(--navy-deep)"/>
      <polygon points="320,0 1060,0 1060,165 800,338 300,150" fill="url(#grunge-gold)"/>
      <polygon points="300,150 800,338 792,350 290,164" fill="var(--navy-deep)"/>
      <polygon points="290,172 780,360 775,366 286,180" fill="var(--gold-pale)"/>
      <polygon points="800,338 1060,165 1060,180 810,346" fill="var(--navy-deep)"/>
      <polygon points="560,515 1060,190 1060,212 592,515" fill="var(--gold-pale)"/>
      <polygon points="0,418 0,405 640,515 600,515" fill="var(--gold-pale)"/>
      <polygon points="0,425 590,515 0,515" fill="var(--navy-deep)"/>
    </svg>

    <svg class="photo" style="left:0;top:0" width="1060" height="515" viewBox="0 0 1060 515" role="img" aria-label="Photo of footballers leaping to mark the ball on a grass field">
      <polygon points="600,515 1060,215 1060,515" fill="url(#field)"/>
    </svg>

    <div class="photo photo--player" role="img" aria-label="Photo of a boy in a red kit kicking a soccer ball"></div>
    <div class="photo photo--ball" role="img" aria-label="Soccer ball"></div>

    <div class="trial-badge">
      <svg width="230" height="230" viewBox="0 0 230 230" aria-hidden="true">
        <defs>
          <linearGradient id="badge-gold" x1="0" y1="0" x2="0" y2="1">
            <stop offset="0" stop-color="#ffd24a"/>
            <stop offset="1" stop-color="#f5a614"/>
          </linearGradient>
        </defs>
        <polygon points="115,5 205,45 225,140 165,222 65,222 5,140 25,45" fill="var(--white)"/>
        <polygon points="115,18 194,53 212,137 159,209 71,209 18,137 36,53" fill="url(#badge-gold)"/>
      </svg>
      <div class="trial-badge__text">
        <div class="trial-badge__row"><span class="trial-badge__num">2</span><span class="trial-badge__unit">week</span></div>
        <div class="trial-badge__label">FREE TRIAL</div>
      </div>
    </div>

    <h1 class="headline">
      <span class="headline__top">WHERE KIDS</span>
      <span class="headline__bottom">ARE CHAMPIONS</span>
    </h1>

    <p class="prize-intro">Chance to win Full Term of</p>
    <p class="prize-box"><span class="prize-box__text">10 WEEKLY SESSIONS</span></p>
    <p class="giveaways">Chance to get giveaways such as tickets to games footballs or other great offers.</p>

    <div class="brand-row">
      <span class="brand-mark"><span class="brand-mark__dot"></span>Bright Tykes</span>
      <span class="brand-mark"><span class="brand-mark__dot"></span>Bright Tykes</span>
      <span class="brand-mark"><span class="brand-mark__dot"></span>Bright Tykes</span>
    </div>

    <div class="booking">
      <div class="booking__label">Book online now at</div>
      <div class="booking__url">www.brighttykesplay.com.au/booking</div>
    </div>
  </main>
</body>
</html>
```